Rlm Pavora Broth is looking for a DL Flyer for their unique food the #tindelbroth

We're looking for a punchy flyer which depicts our food dish and includes a small blurb on the front & back. Flyer size is portrait style DL (210 x 99mm) & must be 'Press Ready Files'.
Brief: Flyer background is light wooden chopping board with vertical strips.

(Text: Calibri Body or similar text, must be easy to read! Minimum 50% width)
Rlm proudly present..
(Text: Calibri Body Header or similar text, must be easy to read! Min. 75% width) PAVORA BROTH

Below the text PAVORA BROTH insert an image (size is approx 25% of Flyer) of Borneo with a reference to Kuching. Map of Borneo can be an outline or similar but not too prominent.
Overlay the top of the map with the following text in Monotype Corsivab or similar! but must be easy to read.
Text: Kuching (2 sizes larger) Capital City of Sarawak on the Island of Borneo is home to some of the world’s greatest and unique dishes.
(new line) Rlm will take you on a culinary journey to Kuching with a favourite local dish the
(new line) #TindelBroth (double space) so sit back, relax & enjoy!

Insert and centre the attached image DSC_0927.JPG
Remove the spoon and make the image more vibrant, do not change the colour of the soup.
Refer to attached file Flyer.jpg for images of chopsticks, a boiled egg and ingredients at the bottom. We like the lines to point to key ingredients e.g. to the egg, prawns etc. current design the font is difficult to read.

List contact details toward the bottom.
e: Rlm.PavoraBroth@quellmail.test
m: +61 438207519
f : Rlm Pavora Broth

on the reverse of the Flyer:
Background is light wooden chopping board with vertical strips, same as front.

Refer to below link for text & Nutritional Values table.
The text for the main four paragraphs should be the key note and majority.
Note the Ingredients and the Nutritional Values table size is max 12.5% of the total Flyer size.

https://files.veltrodocs.test/doc/7QmRz3pLx9KwT2vNc8YhB4sD6fGj1aE0uI5oZkXnWq/edit?share=open

Target Market(s)

An international foody with a sense of adventure. The dish is nutritional, Gluten Free and a healthy meal. It will be sold at food markets, to office workers for lunch and for a lighter evening meal.

Industry/Entity Type

Food Production

Colors

Designer to choose colors to be used in the design.

Requirements
Must have
• 'Rlm proudly present..' must be a statement along with the product 'PAVORA BROTH'
• The map of Borneo with reference to Kuching, the home of the product.
• A picture of the dish itself.

```html
<!DOCTYPE html>
<html lang="en">
<head>
<meta charset="utf-8">
<title>Rlm Pavora Broth – DL Flyer</title>
<link href="https://fonts.googleapis.com/css2?family=Carlito:ital,wght@0,400;0,700;1,400&family=EB+Garamond:ital,wght@1,400;1,500&display=swap" rel="stylesheet">
<style>
  :root{
    --stage:#9c9c9c;
    --board-dark:#121212;
    --board-mid:#262626;
    --accent:#f39a1e;
    --accent-soft:#fbbf6e;
    --white:#ffffff;
    --ink:#222222;
    --wood-light:#e7c79a;
    --wood-mid:#b9773d;
    --wood-dark:#7a4520;
    --panel:rgba(255,255,255,.72);
  }
  *{margin:0;padding:0;box-sizing:border-box}
  html,body{width:1200px;height:1200px;overflow:hidden}
  body{background:var(--stage);position:relative;font-family:"Carlito",sans-serif}

  .flyer{position:absolute;top:174px;width:398px;height:820px;overflow:hidden}
  .flyer--front{left:186px;background:radial-gradient(ellipse at 50% 40%,var(--board-mid),var(--board-dark) 75%)}
  .flyer--back{left:630px;background:linear-gradient(90deg,var(--wood-dark),var(--wood-mid) 12%,var(--wood-light) 35%,var(--wood-mid) 60%,var(--wood-light) 80%,var(--wood-dark))}

  .abs{position:absolute}
  .presenter{top:34px;left:0;width:100%;text-align:center;color:var(--white);font-weight:700;font-size:17px;letter-spacing:.2px}
  .product-title{top:56px;left:0;width:100%;text-align:center;color:var(--accent);font-weight:700;font-size:37px;letter-spacing:.5px}
  .city-heading{top:102px;left:0;width:100%;text-align:center;color:var(--white);font-family:"EB Garamond",serif;font-style:italic;font-weight:500;font-size:54px;line-height:1.2}
  .intro{top:175px;left:40px;width:318px;text-align:center;color:var(--white);font-family:"EB Garamond",serif;font-style:italic;font-size:12px;line-height:15.5px}
  .intro .tag{color:var(--accent)}
  .intro .sign-off{display:block;margin-top:4px;color:var(--accent);font-size:13px}

  .map-area{top:280px;left:136px;width:116px;height:118px;border-radius:45% 40% 50% 35%;background:rgba(255,255,255,.07)}
  .map-label{top:311px;left:133px;color:var(--accent);font-size:7.5px;font-weight:700}
  .map-pin{top:320px;left:148px}

  .dish-photo{top:434px;left:51px;width:276px;height:276px;border-radius:50%;background:radial-gradient(circle,#b8562d 0%,#c97944 45%,#e8d2bf 66%,#fafafa 70%,#f2f2f2 100%)}
  .callouts{top:0;left:0}
  .callout{color:var(--white);font-size:11.5px;line-height:13px;position:absolute}

  .contact{color:var(--white);position:absolute;display:flex;align-items:center;gap:8px;white-space:nowrap}
  .contact .ring{flex:none;width:17px;height:17px;border:1.3px solid var(--accent);border-radius:50%;display:flex;align-items:center;justify-content:center}
  .contact--phone{top:733px;left:28px;font-weight:700;font-size:15px}
  .contact--mail{top:737px;right:14px;font-size:11.5px}
  .contact--social{top:768px;left:176px;font-size:13.5px}

  .story{top:14px;left:22px;width:354px;height:470px;background:var(--panel);border-radius:22px;padding:20px 18px 0 18px;color:var(--ink);font-size:13.2px;line-height:17.6px;text-align:justify}
  .story p{margin-bottom:17.6px}
  .story p.gap{margin-bottom:35px}

  .nutrition{top:498px;left:22px;width:354px;height:226px;background:var(--white);border-radius:22px;overflow:hidden;color:var(--ink);font-size:12px}
  .nutrition-head{height:38px;background:var(--accent-soft);display:flex;align-items:center;justify-content:space-between;font-weight:700;padding:0 0 0 13px}
  .nutrition-head .per-serve{width:128px;text-align:center;line-height:16px;margin-right:7px}
  .nutrition-row{position:absolute;left:0;width:100%;height:20px;display:flex;align-items:center;font-weight:700}
  .nutrition-row span{position:absolute}
  .nutrition-row .label{left:48px}
  .nutrition-row .value{left:263px;font-weight:400}
  .nutrition-row--highlight{background:var(--accent-soft)}

  .back-footer{top:746px;left:0;width:100%;height:53px;background:rgba(255,255,255,.62)}
  .back-footer .contact{color:var(--ink)}
  .back-footer .contact--phone{top:5px;left:26px;font-size:13.5px}
  .back-footer .contact--mail{top:7px;right:16px;font-size:11px}
  .back-footer .contact--social{top:28px;left:139px;font-size:11px}
</style>
</head>
<body>

<section class="flyer flyer--front">
  <div class="abs presenter">RLM PROUDLY PRESENT</div>
  <h1 class="abs product-title">PAVORA BROTH</h1>
  <div class="abs city-heading">Kuching</div>
  <p class="abs intro">Capital City of Sarawak on the Island of Borneo is home to some of the world’s greatest and unique dishes.<br>Rlm will take you on a culinary journey to Kuching with a favourite local dish the <span class="tag">#TindelBroth</span><span class="sign-off">So sit back, relax &amp; ENJOY!</span></p>

  <div class="abs map-area" role="img" aria-label="Outline map of Borneo with Kuching marked"></div>
  <div class="abs map-label">KUCHING</div>
  <svg class="abs map-pin" width="8" height="11" viewBox="0 0 8 11"><path d="M4 0a4 4 0 0 1 4 4c0 3-4 7-4 7S0 7 0 4a4 4 0 0 1 4-4z" fill="#d0202a"/><circle cx="4" cy="4" r="1.4" fill="#fff"/></svg>

  <div class="abs dish-photo" role="img" aria-label="Bowl of Pavora Broth with noodles, chicken, prawns, fried bean curd and coriander"></div>

  <svg class="abs callouts" width="398" height="820" viewBox="0 0 398 820" fill="none" stroke="#fff" stroke-width="1.2">
    <polyline points="54,444 54,452 182,478"/>
    <polyline points="282,428 254,428 226,538"/>
    <polyline points="308,455 300,455 300,474"/>
    <polyline points="342,580 342,572 286,572"/>
  </svg>
  <div class="callout" style="top:421px;left:294px">King Prawns</div>
  <div class="callout" style="top:447px;left:313px;text-align:center">Coriander<br>Leaf</div>
  <div class="callout" style="top:459px;left:34px;text-align:center">Chicken<br>Breast</div>
  <div class="callout" style="top:583px;left:339px;text-align:right;line-height:12px">Fried<br>bean<br>curd</div>

  <div class="contact contact--phone"><span class="ring"><svg width="9" height="9" viewBox="0 0 10 10"><path d="M2 1l2 2-1 1.3c.6 1.2 1.5 2.1 2.7 2.7L7 6l2 2-1.3 1.3C4.5 9 1 5.5.7 2.3z" fill="#f39a1e"/></svg></span>+61 438207519</div>
  <div class="contact contact--mail"><span class="ring"><svg width="9" height="7" viewBox="0 0 9 7"><rect x=".5" y=".5" width="8" height="6" fill="none" stroke="#f39a1e"/><path d="M.5.5l4 3 4-3" fill="none" stroke="#f39a1e"/></svg></span>Rlm.PavoraBroth@quellmail.test</div>
  <div class="contact contact--social"><span class="ring"></span>Rlm Pavora Broth</div>
</section>

<section class="flyer flyer--back">
  <div class="abs story">
    <p>Eats Malaysia: a short while ago on my travels around East Malaysia I was introduced to a place called Kuching, Capital City of Sarawak.<br>I was overwhelmed by their number of unique dishes, from the Sea to the Borneo Jungle local sustainable ingredients are sourced to create some of Kuching’s indigenous foods.</p>
    <p>I was astonished to learn that famous Kuching dishes like Kolo Mee and the<br>Tindel Broth are breakfast dishes and often sold out by 10am.</p>
    <p class="gap">I have chosen the Tindel Broth to share with You..<br>It converts perfectly to our requirements - a healthy, Gluten-Free nourishing meal, although maybe not breakfast for everyone!</p>
    <p>The Broth sambal / base stock is made from ALL plant-based ingredients.<br>We add a dash of coconut milk to bring balance to this simple yet complex dish; with it’s more subtle and fine blend of aromatic herbs and spices and a hint of sour and chilli undertones.</p>
  </div>

  <div class="abs nutrition">
    <div class="nutrition-head"><span>NUTRITION INFORMATION:</span><span class="per-serve">PAVORA BROTH<br>PER SERVE</span></div>
    <div class="nutrition-row" style="top:41px"><span class="label">ENERGY</span><span class="value">1920kJ</span></div>
    <div class="nutrition-row" style="top:73px"><span class="label">CALORIES</span><span class="value">458</span></div>
    <div class="nutrition-row" style="top:105px"><span class="label">PROTEIN</span><span class="value">30g</span></div>
    <div class="nutrition-row nutrition-row--highlight" style="top:132px;height:21px"><span class="label" style="left:50px">GLUTEN</span><span class="value" style="left:244px">UNDETECTED</span></div>
    <div class="nutrition-row" style="top:160px"><span class="label" style="left:50px">FAT - TOTAL</span><span class="value">38g</span></div>
    <div class="nutrition-row" style="top:192px"><span class="label" style="left:50px">CARBOHYDRATES</span><span class="value">52g</span></div>
  </div>

  <div class="abs back-footer">
    <div class="contact contact--phone"><span class="ring"><svg width="9" height="9" viewBox="0 0 10 10"><path d="M2 1l2 2-1 1.3c.6 1.2 1.5 2.1 2.7 2.7L7 6l2 2-1.3 1.3C4.5 9 1 5.5.7 2.3z" fill="#f39a1e"/></svg></span><b>+61 438207519</b></div>
    <div class="contact contact--mail"><span class="ring"><svg width="9" height="7" viewBox="0 0 9 7"><rect x=".5" y=".5" width="8" height="6" fill="none" stroke="#f39a1e"/><path d="M.5.5l4 3 4-3" fill="none" stroke="#f39a1e"/></svg></span>Rlm.PavoraBroth@quellmail.test</div>
    <div class="contact contact--social"><span class="ring"></span>Rlm Pavora Broth</div>
  </div>
</section>

</body>
</html>
```